Business card design and logo for plumbing bussiness

We are wanting a logo for a plumbing business is Queensland Australia. KRV Plumbing and Drainage will be doing works on domestic and commercial sites.
Plumbing, drainage and gas works. We are wanting something that will stand out and be noticed. Colours could be black blue and white but open for suggestions.

Target Market(s)

Builders and home renovators

Industry/Entity Type

Plumbing

Contact Information for Business Card

Miles Dorgan - Director
0417 582 913
miles@krvplumbing.example.com.au
QBCC: 847 2106
ABN: 52 319 407 281

Font styles to use
Sans Serif

Colors
000000

Requirements
Must have
• Clear defined branding

```html
<!DOCTYPE html>
<html lang="en">
<head>
<meta charset="utf-8">
<title>KRV Plumbing and Drainage – Business Card</title>
<link rel="stylesheet" href="https://fonts.googleapis.com/css2?family=Cardo&family=Antonio:wght@700&display=swap">
<style>
  :root {
    --card-bg: #2a2a2e;
    --brand-blue: #235470;
    --brand-blue-shade: #1d4259;
    --ink-dark: #1f1f22;
  }
  html, body {
    margin: 0;
    padding: 0;
    overflow: hidden;
    background: var(--card-bg);
  }
  .card {
    position: relative;
    width: 1200px;
    height: 750px;
    background: var(--card-bg);
    overflow: hidden;
  }
  .brand-name {
    position: absolute;
    left: 0;
    width: 1190px;
    top: 118px;
    margin: 0;
    text-align: center;
    font-family: "Cardo", serif;
    font-weight: 400;
    font-size: 150px;
    line-height: 1;
    color: var(--brand-blue);
  }
  .tagline {
    position: absolute;
    left: 376px;
    top: 328px;
    margin: 0;
    font-family: "Cardo", serif;
    font-weight: 400;
    font-size: 50px;
    line-height: 1;
    letter-spacing: 0.5px;
    color: var(--brand-blue);
    white-space: nowrap;
  }
  .ribbon {
    position: absolute;
    left: 0;
    top: 0;
    width: 1200px;
    height: 750px;
  }
  .ribbon-text {
    position: absolute;
    margin: 0;
    font-family: "Cardo", serif;
    font-weight: 400;
    font-size: 50px;
    line-height: 1;
    color: var(--ink-dark);
    white-space: nowrap;
    letter-spacing: 2.5px;
  }
  .ribbon-text--first { left: 394px; top: 426px; }
  .ribbon-text--second { left: 468px; top: 486px; }
  .contact {
    position: absolute;
    display: flex;
    align-items: center;
    font-family: "Antonio", sans-serif;
    font-weight: 700;
    color: var(--brand-blue);
    white-space: nowrap;
  }
  .contact-icon { flex: none; }
  .contact--licence { left: 14px; top: 621px; gap: 12px; font-size: 42px; letter-spacing: -1px; }
  .contact--phone { left: 364px; top: 624px; gap: 20px; font-size: 42px; letter-spacing: -0.5px; }
  .contact--online { left: 714px; top: 624px; gap: 10px; }
  .online-lines {
    display: flex;
    flex-direction: column;
    align-items: flex-end;
    font-size: 26px;
    letter-spacing: -0.4px;
    line-height: 1.1;
    margin-top: 22px;
  }
</style>
</head>
<body>
<main class="card">
  <h1 class="brand-name">KRV</h1>
  <p class="tagline">Plumbing and Drainage</p>

  <svg class="ribbon" viewBox="0 0 1200 750" aria-hidden="true">
    <rect class="ribbon-band" x="0" y="514" width="1200" height="16" fill="var(--brand-blue)"/>
    <polygon class="ribbon-fold" points="372,408 350,514 350,530 412,530" fill="var(--brand-blue-shade)"/>
    <polygon class="ribbon-fold" points="850,408 870,514 870,530 810,530" fill="var(--brand-blue-shade)"/>
    <polygon class="ribbon-face" points="372,408 850,408 794,576 430,576" fill="var(--brand-blue)"/>
  </svg>
  <p class="ribbon-text ribbon-text--first">Builders and home</p>
  <p class="ribbon-text ribbon-text--second">renovators</p>

  <div class="contact contact--licence">
    <svg class="contact-icon" width="52" height="68" viewBox="0 0 52 68" aria-hidden="true">
      <path d="M26 2C12.7 2 2 12.5 2 25.5 2 42 26 66 26 66s24-24 24-40.5C50 12.5 39.3 2 26 2z" fill="var(--brand-blue)"/>
      <circle cx="26" cy="25" r="9" fill="var(--card-bg)"/>
    </svg>
    <span>QBCC: 847 2106</span>
  </div>

  <div class="contact contact--phone">
    <svg class="contact-icon" width="74" height="64" viewBox="0 0 74 64" aria-hidden="true">
      <path d="M4 20C4 6 70 6 70 20v6H54v-8H20v8H4z" fill="var(--brand-blue)"/>
      <path d="M20 22h34l12 36c1 4-1 6-5 6H13c-4 0-6-2-5-6z" fill="var(--brand-blue)"/>
      <g fill="var(--card-bg)">
        <rect x="27" y="32" width="5" height="5"/><rect x="35" y="32" width="5" height="5"/><rect x="43" y="32" width="5" height="5"/>
        <rect x="27" y="40" width="5" height="5"/><rect x="35" y="40" width="5" height="5"/><rect x="43" y="40" width="5" height="5"/>
        <rect x="27" y="48" width="5" height="5"/><rect x="35" y="48" width="5" height="5"/><rect x="43" y="48" width="5" height="5"/>
      </g>
    </svg>
    <span>0417 582 913</span>
  </div>

  <div class="contact contact--online">
    <svg class="contact-icon" width="64" height="64" viewBox="0 0 64 64" aria-hidden="true">
      <circle cx="32" cy="32" r="30" fill="var(--brand-blue)"/>
      <circle cx="32" cy="32" r="25" fill="none" stroke="var(--card-bg)" stroke-width="2"/>
      <ellipse cx="32" cy="32" rx="11" ry="25" fill="none" stroke="var(--card-bg)" stroke-width="2"/>
      <line x1="7" y1="32" x2="57" y2="32" stroke="var(--card-bg)" stroke-width="2"/>
    </svg>
    <div class="online-lines">
      <span>miles@krvplumbing.example.com.au</span>
      <span>www.krvplumbing.example.com.au</span>
    </div>
  </div>
</main>
</body>
</html>
```